A3 Menus for new international restaurant in Singapore.

Looking for new A3 menu design for indoor & outdoor (beautiful garden and trees) restaurant that caters for expat and local families. International menu, cool jazz vibe, great for couples and families. Restaurant called Brass Cove Parlour. I have attached some of the logos we use. Will consider black and white or color options. Restaurant located on a hill where there were tin mines many years ago, hence the name and branding. Looking for three menus (1) Dinner (2) Lunch (3) weekend brunch.

Target Market(s)

Families, young couples and professionals.

Industry/Entity Type

Restaurant

Font styles to use
Serif
Sans Serif

Requirements
Must have
• All food layout on one side of A3, one for each attached menu. Also a space for drinks list on the back.
Nice to have
• Use some of the logo material we have attached.
Should not have

```html
<!DOCTYPE html>
<html lang="en">
<head>
<meta charset="utf-8">
<title>Brass Cove Parlour – Menus</title>
<link rel="stylesheet" href="https://fonts.googleapis.com/css2?family=Josefin+Sans:ital,wght@0,400;0,700;1,400&display=swap">
<style>
:root{
  --backdrop:#d9d9d9;
  --paper:#ffffff;
  --ink:#111111;
  --soft-ink:#444444;
  --photo-warm-1:#5a2d14;
  --photo-warm-2:#b8743a;
  --photo-warm-3:#e8c9a0;
  --photo-stone-1:#1c1c1c;
  --photo-stone-2:#4a4a42;
  --photo-stone-3:#8a8a80;
}
*{box-sizing:border-box;margin:0;padding:0}
html,body{width:1200px;height:799px;overflow:hidden}
body{background:var(--backdrop);font-family:"Josefin Sans",sans-serif;color:var(--ink);position:relative}
.page{position:absolute;top:75px;height:643px;background:var(--paper);box-shadow:0 2px 8px rgba(0,0,0,.25);overflow:hidden}
.page--food{left:62px;width:438px}
.page--drinks{left:516px;width:430px}
.header-art{position:absolute;left:0;top:0;width:100%}
.wordmark{position:absolute;left:0;right:0;text-align:center;font-weight:700;color:var(--paper);font-size:30px;line-height:.95;letter-spacing:1px;text-transform:uppercase}
.page--food .wordmark{top:24px}
.page--drinks .wordmark{top:24px}
.col{position:absolute;font-size:8px;line-height:9.5px}
.item{display:flex;justify-content:space-between;align-items:flex-end;margin-bottom:5px}
.item-text{max-width:135px}
.item-name{font-weight:700;font-size:8.5px}
.item-price{white-space:nowrap;padding-left:6px}
.page--food .col--left{left:28px;top:155px;width:176px}
.page--food .col--right{left:236px;top:155px;width:176px}
.sweets{position:absolute;left:225px;top:478px;width:213px;height:40px;background:var(--ink);color:var(--paper);border-radius:10px 0 0 10px;padding:4px 18px 0 12px;font-size:8px;line-height:10px}
.sweets .item{margin-bottom:1px}
.sweets .item-name{font-size:8px}
.rule{position:absolute;left:0;width:100%;border-top:1px solid var(--ink)}
.special-title{position:absolute;left:0;width:300px;top:535px;text-align:center;font-style:italic;font-weight:700;font-size:9.5px;letter-spacing:.5px}
.special{position:absolute;left:80px;top:553px;width:200px;font-size:8px;line-height:9.5px}
.footnote{position:absolute;left:0;right:0;top:613px;text-align:center;font-style:italic;font-size:6.5px;color:var(--soft-ink)}
.drink-col{position:absolute;top:248px;width:145px;font-size:7.5px;line-height:8.8px}
.drink-col--a{left:36px}
.drink-col--b{left:248px}
.drink-group{margin-bottom:16px}
.drink-heading{font-weight:700;font-size:8px;margin-bottom:6px}
.drink{display:flex;justify-content:space-between}
.drink b{font-weight:700}
.footer-rule{position:absolute;left:0;width:100%;top:605px}
</style>
</head>
<body>

<section class="page page--food" aria-label="Food menu">
  <svg class="header-art" width="438" height="150" viewBox="0 0 438 150">
    <defs>
      <linearGradient id="warmPhoto" x1="0" y1="0" x2="1" y2="1">
        <stop offset="0" stop-color="var(--photo-warm-3)"/>
        <stop offset=".45" stop-color="var(--photo-warm-2)"/>
        <stop offset="1" stop-color="var(--photo-warm-1)"/>
      </linearGradient>
    </defs>
    <rect width="438" height="120" fill="url(#warmPhoto)" role="img" aria-label="Photograph of golden waffles topped with fresh berries and syrup"/>
    <path d="M0 82 Q219 150 438 82 L438 150 L0 150 Z" fill="var(--ink)"/>
    <path d="M0 98 Q219 162 438 98 L438 150 L0 150 Z" fill="var(--paper)"/>
    <circle cx="46" cy="122" r="17" fill="var(--ink)"/>
    <ellipse cx="46" cy="116" rx="4" ry="6" fill="var(--paper)"/>
    <rect x="45" y="121" width="2" height="12" fill="var(--paper)"/>
    <circle cx="392" cy="122" r="17" fill="var(--ink)"/>
    <rect x="386" y="110" width="1.5" height="8" fill="var(--paper)"/>
    <rect x="389.5" y="110" width="1.5" height="8" fill="var(--paper)"/>
    <rect x="393" y="110" width="1.5" height="8" fill="var(--paper)"/>
    <rect x="396.5" y="110" width="1.5" height="8" fill="var(--paper)"/>
    <rect x="386" y="117" width="12" height="3" fill="var(--paper)"/>
    <rect x="391" y="119" width="2" height="14" fill="var(--paper)"/>
  </svg>
  <h1 class="wordmark">Brass Cove<br>Parlour</h1>

  <div class="col col--left">
    <div class="item"><div class="item-text"><span class="item-name">Brass Cove Parlour Muesli and Yoghurt</span><br>with fruit compote</div><span class="item-price">$9.50</span></div>
    <div class="item"><div class="item-text"><span class="item-name">Waffle</span> served with mixed fruit, maple syrup and crushed nuts</div><span class="item-price">$14</span></div>
    <div class="item"><div class="item-text"><span class="item-name">Scrambled Eggs</span> on sour dough toast, with roast tomato, portobello mushroom and chives</div><span class="item-price">$13.50</span></div>
    <div class="item"><div class="item-text"><span class="item-name">Baked Gypsy Eggs</span><br>with rustic napolitano sauce, peas and diced pan-fried potato</div><span class="item-price">$15.50</span></div>
    <div class="item"><div class="item-text"><span class="item-name">Brass Cove Parlour Eggs Benedict</span><br>poached eggs served with either pulled pork or smoked salmon, served on toasted fresh brioche with paprika hollandaise and tomato confit</div><span class="item-price">$16</span></div>
    <div class="item"><div class="item-text"><span class="item-name">The Big Breakfast</span> a choice of sunny-side up, over-easy or scrambled eggs, grilled bacon &amp; pork sausage, tomato, portobello mushroom, baked beans &amp; sourdough toast</div><span class="item-price">$24</span></div>
    <div class="item"><div class="item-text"><span class="item-name">Double Egg &amp; Bacon</span><br>two eggs fried or scrambled, bacon, roast tomato and sourdough toast</div><span class="item-price">$16</span></div>
    <div class="item"><div class="item-text"><span class="item-name">Classic Greek Salad</span><br>with cherry tomatoes, feta, kalamata olives, green capsicum &amp; cucumber</div><span class="item-price">$14.50</span></div>
    <div class="item"><div class="item-text"><span class="item-name">Brass Cove Parlour Garden Salad</span><br>with mesclun leaves, cherry tomatoes, kalamata olives, shaved parmesan, classic vinaigrette and croutons</div><span class="item-price">$12</span></div>
  </div>

  <div class="col col--right">
    <div class="item"><div class="item-text"><span class="item-name">Strigoli</span> with beef ragu bolognese</div><span class="item-price">$16</span></div>
    <div class="item"><div class="item-text"><span class="item-name">Linguini</span><br>in a light creamy carbonara sauce, with smoked pancetta</div><span class="item-price">$17</span></div>
    <div class="item"><div class="item-text"><span class="item-name">Rigatoni</span><br>with aglio, olio and pepperoncino<br>with prawns, add</div><span class="item-price">$15<br>$5</span></div>
    <div class="item"><div class="item-text"><span class="item-name">Roast Pork Belly Ciabatta</span><br>with arugula, wholegrain mustard and apple cider sauce, served with fries</div><span class="item-price">$16</span></div>
    <div class="item"><div class="item-text"><span class="item-name">Roast Beef Ciabatta</span><br>with cheddar cheese, tomato and lettuce, served with fries</div><span class="item-price">$17</span></div>
    <div class="item"><div class="item-text"><span class="item-name">Brass Cove Parlour Bangers &amp; Mash</span><br>prime pork sausages, buttery mashed potato covered in onion &amp; cider gravy</div><span class="item-price">$17</span></div>
    <div class="item"><div class="item-text"><span class="item-name">Beer Battered Fish &amp; Chips</span><br>with homemade tartar sauce and mushy peas</div><span class="item-price">$17</span></div>
    <div class="item"><div class="item-text"><span class="item-name">Brass Cove Parlour Burger</span><br>200gms ground prime beef, in a homemade brioche bun with lettuce, tomato and mayo, and a side of fries<br>Top it with cheese or bacon or both – add</div><span class="item-price">$20<br><br>$2 for each</span></div>
  </div>

  <div class="sweets">
    <div class="item"><div class="item-text"><span class="item-name">Selection of freshly baked cakes and tarts</span> each</div><span class="item-price">$9</span></div>
    <div class="item"><div class="item-text"><span class="item-name">Ice Cream</span> per scoop</div><span class="item-price">$5</span></div>
  </div>

  <div class="rule" style="top:527px"></div>
  <h2 class="special-title">SUNDAY LUNCH SPECIAL</h2>
  <div class="special item"><div class="item-text" style="max-width:160px"><span class="item-name">Brass Cove Parlour Roast</span><br>roast beef sirloin with all the trimmings, yorkshire pudding and gravy</div><span class="item-price">$32.50</span></div>
  <div class="rule" style="top:603px"></div>
  <p class="footnote">All prices are in Singapore Dollars and are subject to GST &amp; 10% Service Charge</p>
</section>

<section class="page page--drinks" aria-label="Drinks menu">
  <svg class="header-art" width="430" height="185" viewBox="0 0 430 185">
    <defs>
      <linearGradient id="stonePhoto" x1="0" y1="0" x2="1" y2="1">
        <stop offset="0" stop-color="var(--photo-stone-1)"/>
        <stop offset=".55" stop-color="var(--photo-stone-2)"/>
        <stop offset="1" stop-color="var(--photo-stone-3)"/>
      </linearGradient>
    </defs>
    <rect width="430" height="160" fill="url(#stonePhoto)" role="img" aria-label="Close-up photograph of dark tin ore crystals"/>
    <path d="M0 98 Q215 215 430 98 L430 185 L0 185 Z" fill="var(--ink)"/>
    <path d="M0 112 Q215 225 430 112 L430 185 L0 185 Z" fill="var(--paper)"/>
    <circle cx="166" cy="155" r="18" fill="var(--ink)"/>
    <circle cx="215" cy="157" r="18" fill="var(--ink)"/>
    <circle cx="264" cy="155" r="18" fill="var(--ink)"/>
  </svg>
  <h1 class="wordmark">Brass Cove<br>Parlour</h1>

  <div class="drink-col drink-col--a">
    <div class="drink-group">
      <div class="drink-heading">MINERAL WATER</div>
      <div class="drink"><span>fonte chiara 500ml</span><span>$6</span></div>
      <div class="drink"><span>fonte chiara 500ml still</span><span>$6</span></div>
    </div>
    <div class="drink-group">
      <div class="drink-heading">JUICES</div>
      <div class="drink"><span><b>Orange</b> juice</span><span>$4.50</span></div>
      <div class="drink"><span><b>Apple</b> juice</span><span>$4.50</span></div>
      <div class="drink"><span><b>Tomato</b> juice</span><span>$4.50</span></div>
      <div class="drink"><span><b>Cranberry</b> juice</span><span>$5</span></div>
      <div class="drink"><span><b>Pineapple</b> juice</span><span>$4</span></div>
    </div>
    <div class="drink-group">
      <div class="drink-heading">SOFT DRINKS</div>
      <div class="drink"><span><b>Cola</b></span><span>$4</span></div>
      <div class="drink"><span><b>Diet</b> cola</span><span>$4</span></div>
      <div class="drink"><span><b>Cola</b> zero</span><span>$4</span></div>
      <div class="drink"><span><b>Lemon</b> squash</span><span>$4</span></div>
      <div class="drink"><span><b>Lemonade</b></span><span>$4</span></div>
      <div class="drink"><span><b>Pink</b> lemonade</span><span>$4</span></div>
      <div class="drink"><span><b>Tonic</b> water</span><span>$4</span></div>
      <div class="drink"><span><b>Bitter</b> lemon</span><span>$4</span></div>
      <div class="drink"><span><b>Dry</b> ginger ale</span><span>$4</span></div>
      <div class="drink"><span><b>Lemon</b> lime bitters</span><span>$5</span></div>
    </div>
  </div>

  <div class="drink-col drink-col--b">
    <div class="drink-group">
      <div class="drink-heading">MINERAL WATER</div>
      <div class="drink"><span>fonte chiara 500ml</span><span>$6</span></div>
      <div class="drink"><span>fonte chiara 500ml still</span><span>$6</span></div>
    </div>
    <div class="drink-group">
      <div class="drink-heading">JUICES</div>
      <div class="drink"><span><b>Orange</b> juice</span><span>$4.50</span></div>
      <div class="drink"><span><b>Apple</b> juice</span><span>$4.50</span></div>
      <div class="drink"><span><b>Tomato</b> juice</span><span>$4.50</span></div>
      <div class="drink"><span><b>Cranberry</b> juice</span><span>$5</span></div>
      <div class="drink"><span><b>Pineapple</b> juice</span><span>$4</span></div>
    </div>
    <div class="drink-group">
      <div class="drink-heading">SOFT DRINKS</div>
      <div class="drink"><span><b>Cola</b></span><span>$4</span></div>
      <div class="drink"><span><b>Diet</b> cola</span><span>$4</span></div>
      <div class="drink"><span><b>Cola</b> zero</span><span>$4</span></div>
      <div class="drink"><span><b>Lemon</b> squash</span><span>$4</span></div>
      <div class="drink"><span><b>Lemonade</b></span><span>$4</span></div>
      <div class="drink"><span><b>Pink</b> lemonade</span><span>$4</span></div>
      <div class="drink"><span><b>Tonic</b> water</span><span>$4</span></div>
      <div class="drink"><span><b>Bitter</b> lemon</span><span>$4</span></div>
      <div class="drink"><span><b>Dry</b> ginger ale</span><span>$4</span></div>
      <div class="drink"><span><b>Lemon</b> lime bitters</span><span>$5</span></div>
    </div>
  </div>

  <svg class="footer-rule" width="430" height="30" viewBox="0 0 430 30">
    <line x1="0" y1="15" x2="430" y2="15" stroke="var(--ink)" stroke-width="1"/>
    <circle cx="215" cy="15" r="14" fill="var(--ink)"/>
  </svg>
</section>

</body>
</html>
```